Young Architect Bussiness Card

English is not my first language (spanish is).
Need a bussiness card design for my best friend who is about to graduate from college, Licentiate degree in architecture, so she needs business cards to start networking, currently she has no porfolio, web page or facebook. so she is relying on her cel phone and gmail, but should leave space for one of them (facebook)

Design for business card should be modern, maybe something with construction blue prints patern or 3D modelling.

Name: Mariela Ocampo Valverde
Licentiate in Arquitecture
Cel: (506) XXX-8270
email: marielaXXX@correonube.net

Services, although im not sure if it has to be there or not:
Anteproyectos / Proposal design
Inspecciones / Site Inspections
Modelado 3D / 3D modelling
Planos Constructivos / Construction Blue Prints
Presupuestos / Budgets

Design should be in spanish

Industry/Entity Type

Architect

Contact Information for Business Card

Name: Mariela Ocampo, Arquitecto
Associtation code : XXXX
Phone: (506) XXXX-XXXX
Email: xxx@correonube.net
Facebook: xxxx

Requirements
Must have
• Design for business card should be modern, maybe something with construction blue prints patern or 3D modelling.
Nice to have
• Something like a transition from 2D to 3D.

```html
<!DOCTYPE html>
<html lang="es">
<head>
<meta charset="utf-8">
<title>Tarjeta de presentación — Mariela Ocampo Valverde</title>
<link rel="stylesheet" href="https://fonts.googleapis.com/css2?family=Libre+Franklin:wght@400;700&display=swap">
<style>
  :root {
    --stage: #999999;
    --paper: #f2f3f5;
    --navy: #163f77;
    --ink-blue: #1f3f78;
    --accent-red: #d41243;
    --white: #ffffff;
  }
  html, body {
    margin: 0;
    width: 1073px;
    height: 1200px;
    overflow: hidden;
    background: var(--stage);
  }
  .stage {
    position: relative;
    width: 1073px;
    height: 1200px;
  }
  .card {
    position: absolute;
    left: 153px;
    width: 791px;
    display: block;
    font-family: "Libre Franklin", Arial, sans-serif;
  }
  .card--front { top: 136px; height: 455px; }
  .card--back  { top: 629px; height: 458px; }

  .card__blueprint { fill: url(#blueprintTone); }
  .card__blueprint--back { fill: url(#blueprintToneBack); }
  .card__band { fill: var(--navy); }

  .service { font-size: 23px; font-weight: 400; }
  .service--es { fill: var(--white); }
  .service--en { fill: var(--ink-blue); }

  .holder-name { fill: var(--ink-blue); font-size: 34px; font-weight: 700; }
  .holder-title { fill: var(--accent-red); font-size: 25px; font-weight: 700; }
  .contact-text { fill: var(--white); font-size: 18px; font-weight: 400; }
  .contact-icon-box { fill: var(--white); }
  .contact-icon-line { fill: none; stroke: var(--navy); stroke-width: 2.4; stroke-linejoin: round; }
  .contact-icon-fill { fill: var(--navy); }
</style>
</head>
<body>
<main class="stage">

  <!-- Front: services -->
  <svg class="card card--front" viewBox="0 0 791 455" aria-label="Servicios">
    <defs>
      <linearGradient id="blueprintTone" x1="0" y1="0" x2="1" y2="1">
        <stop offset="0" stop-color="#f4f5f7"/>
        <stop offset="1" stop-color="#e8eaee"/>
      </linearGradient>
    </defs>
    <rect class="card__blueprint" x="0" y="0" width="791" height="455" role="img" aria-label="Plano arquitectónico tenue de fondo con escalera y cortes constructivos"/>
    <polygon class="card__band" points="0,0 273,0 518,455 0,455"/>

    <g class="services services--es">
      <text class="service service--es" transform="translate(176 285) rotate(-29)">Anteproyectos</text>
      <text class="service service--es" transform="translate(199 310) rotate(-29)">Inspecciones</text>
      <text class="service service--es" transform="translate(217 342) rotate(-29)">Modelado 3D</text>
      <text class="service service--es" transform="translate(150 418) rotate(-29)">Planos Constructivos</text>
      <text class="service service--es" transform="translate(248 410) rotate(-29)">Presupuestos</text>
    </g>

    <g class="services services--en">
      <text class="service service--en" transform="translate(392 166) rotate(-29)">Proposal design</text>
      <text class="service service--en" transform="translate(411 200) rotate(-29)">Site Inspections</text>
      <text class="service service--en" transform="translate(429 231) rotate(-29)">3D modelling</text>
      <text class="service service--en" transform="translate(448 262) rotate(-29)">Construction Blue Prints</text>
      <text class="service service--en" transform="translate(463 294) rotate(-29)">Budgets</text>
    </g>
  </svg>

  <!-- Back: name and contact -->
  <svg class="card card--back" viewBox="0 0 791 458" aria-label="Datos de contacto">
    <defs>
      <linearGradient id="blueprintToneBack" x1="0" y1="0" x2="1" y2="1">
        <stop offset="0" stop-color="#f4f5f7"/>
        <stop offset="1" stop-color="#e8eaee"/>
      </linearGradient>
    </defs>
    <rect class="card__blueprint card__blueprint--back" x="0" y="0" width="791" height="458" role="img" aria-label="Plano arquitectónico tenue de fondo con cubierta y vigas en diagonal"/>
    <polygon class="card__band" points="291,0 791,0 791,458 536,458"/>

    <g class="holder">
      <text class="holder-name" x="210" y="245" text-anchor="middle">Mariela Ocampo</text>
      <text class="holder-name" x="214" y="291" text-anchor="middle">Valverde</text>
      <text class="holder-title" x="230" y="372" text-anchor="middle">Licentiate in Arquitecture</text>
    </g>

    <g class="contact">
      <text class="contact-text" x="714" y="321" text-anchor="end">marielaXXX@correonube.net</text>
      <g class="contact-icon contact-icon--mail">
        <rect class="contact-icon-box" x="733" y="298" width="34" height="34" rx="3"/>
        <rect class="contact-icon-line" x="738" y="305" width="24" height="19"/>
        <polyline class="contact-icon-line" points="738,305 750,316 762,305"/>
      </g>

      <text class="contact-text" x="714" y="373" text-anchor="end">(506) XXX-8270</text>
      <g class="contact-icon contact-icon--phone">
        <rect class="contact-icon-box" x="733" y="350" width="34" height="34" rx="5"/>
        <path class="contact-icon-fill" d="M741 356 l6 0 l2 7 l-4 3 q3 6 9 9 l3 -4 l7 2 l0 6 q-2 2 -5 2 q-19 -3 -20 -20 q0 -3 2 -5 z"/>
      </g>

      <text class="contact-text" x="714" y="427" text-anchor="end">marielaXXX</text>
      <rect class="contact-icon-box contact-icon--social" x="733" y="404" width="34" height="34" rx="3"/>
    </g>
  </svg>

</main>
</body>
</html>
```